Wall graphic, will be projected on wall and repainted by owners

We would like to paint a design, 2D illustration on the wall. I have posted a picture of our logo we painted on the adjacent wall. We use a projector from the design and trace it on. So this would need to be fairly simple and not too many colors.

We are a gym, so the design would be something to do with:

Some ideas, not limited to...

achievement, fitness, Olympic lifting, barbells, sport, goals, etc.

- 10 fitness skills; https://www.brovantix.com/mt-archive2/000056.html#/comments

-Brovantix hierarchy of development

Constantly Varied, High Intensity, Functional Movement

"You against You."

"Ordinary People doing extraordinary Things"

Scalable...Prepared for everyday life; push, pull, run, Jump, throwing, picking things up

The rig has a mountainous look to it, so it could play on that. You can also use the door as you wish, the 'Exit' sign must stay.

The design can go some what outside of the rig(structure), but not really much above it

To add a few comments from other owner:

Primal theme; caveman; paleo; fundamentals...

Target Market(s)

21 - 55 years old, motivated, chill, men and women.

Industry/Entity Type

Fitness

Font styles to use
Sans Serif
Other font styles liked:
• PowerCord

Requirements
Must have
• low complexity, must be able to be traced and re-created on the wall
Nice to have
• Can integrate "Shaping Bold Vigor" or some cursive words relating to athletics, Brovantix, Olympic lifting, etc.
• Idea that BroVantix is for anyone, it helps to improve everyday life.
• The primal concept; caveman, paleo, fundamentals.
Should not have
• too many colors.

```html
<!DOCTYPE html>
<html lang="en">
<head>
<meta charset="utf-8">
<title>Shaping Bold Vigor — Wall Graphic</title>
<link rel="stylesheet" href="https://fonts.googleapis.com/css2?family=Black+Ops+One&family=Graduate&family=Oswald:wght@500;700&family=Teko:wght@400&family=Bungee&display=swap">
<style>
  :root {
    --ink: #000000;
    --paper: #ffffff;
    --figure-top: #1a1a1a;
    --figure-bottom: #000000;
    --rule: 3px;
  }
  * { box-sizing: border-box; margin: 0; padding: 0; }
  html, body { width: 1200px; height: 555px; overflow: hidden; background: var(--paper); }
  .wall {
    position: relative; width: 1200px; height: 555px;
    background: var(--paper); color: var(--ink);
    border: var(--rule) solid var(--ink); overflow: hidden;
  }
  .panel { position: absolute; border: var(--rule) solid var(--ink); overflow: hidden; }
  .figure {
    position: absolute; z-index: 0;
    background: linear-gradient(180deg, var(--figure-top), var(--figure-bottom));
    border-radius: 40px 40px 8px 8px;
  }
  .centered { position: absolute; z-index: 1; text-align: center; white-space: nowrap; }

  /* muscle panel */
  .muscle { left: 0; top: 0; width: 432px; height: 110px; }
  .muscle__text {
    left: 122px; width: 304px; top: 18px; font-family: "Oswald", sans-serif;
    font-weight: 700; font-size: 21px; line-height: 38px;
  }

  /* strength panel */
  .strength { left: 0; top: 108px; width: 288px; height: 447px; }
  .strength__text {
    left: 0; right: 0; top: 24px; font-family: "Black Ops One", sans-serif;
    font-size: 24px; line-height: 36px;
  }
  .strength__text .balance { border-bottom: 3px solid var(--ink); padding: 0 4px; }

  /* lifting stat panel */
  .lifting { left: 286px; top: 108px; width: 148px; height: 447px; }
  .lifting__text {
    left: 0; right: 0; top: 10px; font-family: "Black Ops One", sans-serif;
    font-size: 12px; line-height: 14px;
  }
  .lifting__num { display: inline-block; background: var(--ink); color: var(--paper); font-size: 15px; line-height: 15px; padding: 0 5px; }
  .lifting__bar {
    left: 0; right: 0; top: 70px; height: 24px; background: var(--ink); color: var(--paper);
    font-family: "Black Ops One", sans-serif; font-size: 19px; line-height: 24px;
  }

  /* slogan badge */
  .badge { left: 432px; top: 0; width: 272px; height: 202px; }
  .badge__shape { position: absolute; left: 46px; top: 6px; }
  .badge__text {
    left: 0; right: 0; top: 44px; color: var(--paper);
    font-family: "Graduate", sans-serif; font-size: 25px; line-height: 36px;
    -webkit-text-stroke: 0.8px var(--paper);
  }

  /* develops panel */
  .develops { left: 432px; top: 200px; width: 272px; height: 148px; }
  .develops__head {
    left: 0; right: 0; top: 2px; height: 38px; background: var(--ink); color: var(--paper);
    font-family: "Oswald", sans-serif; font-weight: 500; font-size: 27px; line-height: 38px;
    letter-spacing: 0.5px;
  }
  .develops__split { position: absolute; left: 0; right: 0; top: 66px; bottom: 0; border-top: var(--rule) solid var(--ink); display: flex; }
  .develops__item {
    flex: 1; display: flex; align-items: center; justify-content: center; text-align: center;
    font-family: "Oswald", sans-serif; font-weight: 500; font-size: 20px; line-height: 26px;
  }
  .develops__item + .develops__item { border-left: var(--rule) solid var(--ink); }

  .tire { left: 432px; top: 346px; width: 272px; height: 209px; }

  /* core panel */
  .core { left: 702px; top: 0; width: 498px; height: 194px; }
  .core__text {
    left: 108px; right: 4px; top: 30px; font-family: "Graduate", sans-serif;
    font-size: 38px; line-height: 44px; -webkit-text-stroke: 1.2px var(--ink);
  }

  /* ego panel */
  .ego { left: 702px; top: 192px; width: 498px; height: 122px; }
  .ego__text {
    position: absolute; z-index: 1; left: 6px; top: 8px; font-family: "Teko", sans-serif;
    font-weight: 400; font-size: 68px; line-height: 54px; letter-spacing: 2px; white-space: nowrap;
  }
  .ego__text em { font-size: 50px; }

  /* prevent panel */
  .prevent { left: 702px; top: 312px; width: 250px; height: 243px; }
  .prevent__title {
    position: absolute; z-index: 1; left: 6px; top: 0; font-family: "Oswald", sans-serif;
    font-weight: 700; font-size: 44px; line-height: 52px;
  }
  .prevent__list { position: absolute; z-index: 1; left: 2px; top: 54px; width: 176px; list-style: none; }
  .prevent__list li {
    height: 33px; margin-bottom: 1px; text-align: center; border: 2px solid var(--ink);
    font-family: "Oswald", sans-serif; font-weight: 700; font-size: 25px; line-height: 29px;
  }
  .prevent__list li.dark { background: var(--ink); color: var(--paper); }
  .prevent__cta {
    position: absolute; z-index: 1; left: 8px; top: 212px; font-family: "Oswald", sans-serif;
    font-weight: 700; font-size: 15px;
  }

  /* progression panel */
  .progress { left: 950px; top: 312px; width: 250px; height: 243px; }
  .progress__text { position: absolute; z-index: 1; left: 2px; top: 8px; font-family: "Bungee", sans-serif; }
  .progress__text span { display: block; white-space: nowrap; }
  .progress__one { font-size: 29px; line-height: 36px; }
  .progress__two { font-size: 50px; line-height: 58px; }
  .progress__three { font-size: 21px; line-height: 30px; }
</style>
</head>
<body>
<main class="wall">

  <section class="panel muscle">
    <div class="figure" style="left:4px;top:4px;width:112px;height:96px;border-radius:50px 10px 10px 50px" role="img" aria-label="Silhouette of an athlete doing a pike on a stability ball"></div>
    <p class="centered muscle__text">MUSCLE CONTRACTS AND<br>SHORTENS AT A CONSTANT SPEED</p>
  </section>

  <section class="panel strength">
    <p class="centered strength__text">STRENGTH TRAINING<br>CAN <span class="balance">BALANCE</span><br>GLUCOSE LEVELS</p>
    <div class="figure" style="left:72px;top:150px;width:128px;height:289px" role="img" aria-label="Silhouette of a woman doing a barbell back squat"></div>
  </section>

  <section class="panel lifting">
    <p class="centered lifting__text">ADDING JUST <span class="lifting__num">2</span><br>LIFTING SESSIONS<br>A WEEK CAN<br>REDUCE BODY</p>
    <p class="centered lifting__bar">FAT BY 7%</p>
    <div class="figure" style="left:10px;top:104px;width:116px;height:332px" role="img" aria-label="Silhouette of a man pressing a kettlebell overhead"></div>
  </section>

  <section class="panel badge">
    <svg class="badge__shape" width="176" height="176" viewBox="0 0 176 176" aria-hidden="true">
      <polygon points="88,2 121,8 149,27 168,55 174,88 168,121 149,149 121,168 88,174 55,168 27,149 8,121 2,88 8,55 27,27 55,8" fill="var(--ink)"/>
      <polygon points="88,14 116,20 140,36 156,60 162,88 156,116 140,140 116,156 88,162 60,156 36,140 20,116 14,88 20,60 36,36 60,20" fill="none" stroke="var(--paper)" stroke-width="2"/>
    </svg>
    <p class="centered badge__text">SHAPING<br>BOLD<br>VIGOR</p>
  </section>

  <section class="panel develops">
    <p class="centered develops__head">BROVANTIX DEVELOPS</p>
    <div class="develops__split">
      <p class="develops__item">NEUROLOGICAL<br>FITNESS</p>
      <p class="develops__item">PHYSICAL<br>SKILLS</p>
    </div>
  </section>

  <section class="panel tire">
    <div class="figure" style="left:4px;top:4px;width:258px;height:196px;border-radius:30px 60px 8px 8px" role="img" aria-label="Silhouette of an athlete flipping a large tractor tire"></div>
  </section>

  <section class="panel core">
    <div class="figure" style="left:2px;top:2px;width:100px;height:184px;border-radius:6px" role="img" aria-label="Silhouette of an athlete hanging from a pull-up bar"></div>
    <p class="centered core__text">STRONGER CORE<br>=<br>BETTER POSTURE</p>
  </section>

  <section class="panel ego">
    <p class="ego__text">LEAVE YOUR <em>EGO</em><br>AT THE DOOR</p>
    <div class="figure" style="left:372px;top:12px;width:110px;height:100px;border-radius:40px 40px 6px 6px" role="img" aria-label="Silhouette of a woman lunging while holding a medicine ball"></div>
  </section>

  <section class="panel prevent">
    <p class="prevent__title">PREVENT</p>
    <ul class="prevent__list">
      <li class="dark">OBESITY</li>
      <li>ARTHRITIS</li>
      <li class="dark">DIABETES</li>
      <li>DEPRESSION</li>
    </ul>
    <p class="prevent__cta">...SO GET MOVING</p>
    <div class="figure" style="left:182px;top:4px;width:60px;height:232px" role="img" aria-label="Silhouette of a woman holding a kettlebell overhead"></div>
  </section>

  <section class="panel progress">
    <p class="progress__text">
      <span class="progress__one">PROGRESSION</span>
      <span class="progress__two">NOT</span>
      <span class="progress__three">PERFECTION</span>
    </p>
    <div class="figure" style="left:166px;top:110px;width:76px;height:126px;border-radius:30px 10px 6px 6px" role="img" aria-label="Silhouette of a man doing bench dips on a box"></div>
  </section>

</main>
</body>
</html>
```